Fuelo Fuel Delivery Truck Wrap

We need a clean-cut, modern truck wrap design for a 2020 extended cab R-340 truck with an 8-foot long bed. We are an app-based, on-demand fuel delivery service that will deliver gasoline or diesel directly to the end user at their home, work, school, gym, etc. We would like for the trucks to be blue (#04B2FF) with graphics on top of that color. The final design should be clean, modern, and convey information such as one or more of the tag lines listed below (you can choose which tag lines to use or exclude), website, download available on appnest/storeva, and the correct placards for hauling hazardous materials (1203, class 3). | Website: www.fuelo-example.us | Possible tag lines: Gas...Delivered, #PumpAnew, Say Goodbye to the Gas Station |

Target Market(s)

Business people, college students

Industry/Entity Type

Oil And Gas

Font styles to use
Sans Serif

Colors

Designer to choose colors to be used in the design.

Requirements
Must have
• HAZMAT Placards, website, Appnest/ Storeva logos, tag lines.
Nice to have
• Stick out. When people see this truck, we want them to know exactly whose truck they are looking at. Ex: When you see a KRV truck, you know exactly what it is. When people see this truck, they should know that it is Fuelo's truck.

```html
<!DOCTYPE html>
<html lang="en">
<head>
<meta charset="utf-8">
<title>Fuelo Truck Wrap – Side Layouts</title>
<link href="https://fonts.googleapis.com/css2?family=Quicksand:wght@500;600;700&family=Lato:wght@400;700&family=Lobster&display=swap" rel="stylesheet">
<style>
  :root{
    --wrap-blue:#45a8dc;
    --wrap-white:#e9e9ea;
    --glass:#2b2f33;
    --stage:#000000;
    --placard-red:#e3262f;
    --badge-black:#0b0b0b;
  }
  html,body{margin:0;padding:0;width:1200px;height:854px;overflow:hidden;background:var(--stage);}
  .wrap-sheet{display:block;width:1200px;height:854px;}
  .body-panel{fill:var(--wrap-blue);}
  .window-area{fill:var(--glass);}
  .brand-band{fill:var(--wrap-white);}
  .tagline-panel{fill:var(--wrap-white);}
  .accent-stripe{fill:var(--wrap-white);}
  .wordmark{font-family:"Quicksand",sans-serif;font-weight:600;font-size:128px;fill:var(--wrap-white);}
  .slogan{font-family:"Lato",sans-serif;font-weight:400;font-size:22px;letter-spacing:9px;fill:var(--wrap-white);}
  .website{font-family:"Lato",sans-serif;font-weight:700;font-size:18px;fill:var(--wrap-blue);}
  .tagline{font-family:"Lobster",cursive;font-size:19px;fill:var(--wrap-blue);}
  .app-note{font-family:"Lato",sans-serif;font-style:italic;font-size:12px;fill:#ffffff;}
  .store-badge{fill:var(--badge-black);stroke:#9a9a9a;stroke-width:.6;}
  .store-name{font-family:"Lato",sans-serif;font-weight:700;font-size:12px;fill:#ffffff;}
  .placard-diamond{fill:var(--placard-red);stroke:#ffffff;stroke-width:2;}
  .placard-number-box{fill:#ffffff;}
  .placard-number{font-family:"Lato",sans-serif;font-weight:700;font-size:14px;fill:#111111;}
  .placard-class{font-family:"Lato",sans-serif;font-weight:700;font-size:8px;fill:#ffffff;}
</style>
</head>
<body>
<svg class="wrap-sheet" viewBox="0 0 1200 854" xmlns="http://www.w3.org/2000/svg">
  <defs>
    <path id="truck-side" d="M45,175 L300,150 L380,55 L640,48 L652,148 L1138,140 L1142,290 L1016,292 A76,76 0 0 0 864,292 L242,302 A76,76 0 0 0 92,302 L45,298 Z"/>
    <polygon id="truck-glass" points="312,160 392,66 608,62 612,150 318,162"/>
    <clipPath id="clip-driver-side"><use href="#truck-side"/></clipPath>
    <clipPath id="clip-passenger-side"><use href="#truck-side" transform="translate(1204 428) scale(-1 1)"/></clipPath>
  </defs>

  <!-- Driver side layout -->
  <g class="layout-driver-side">
    <g clip-path="url(#clip-driver-side)">
      <use href="#truck-side" class="body-panel"/>
      <rect class="brand-band" x="235" y="40" width="250" height="270"/>
      <polygon class="tagline-panel" points="842,146 978,144 988,246 848,248"/>
      <polygon class="accent-stripe" points="832,146 837,146 843,248 838,248"/>
      <polygon class="accent-stripe" points="984,144 990,144 1000,270 994,270"/>
      <use href="#truck-glass" class="window-area"/>
    </g>
    <g class="hazmat-placard" transform="translate(174 192)">
      <rect class="placard-diamond" x="-19" y="-19" width="38" height="38" transform="rotate(45)"/>
      <rect class="placard-number-box" x="-17" y="-10" width="34" height="17"/>
      <text class="placard-number" x="0" y="4" text-anchor="middle">1203</text>
      <text class="placard-class" x="0" y="20" text-anchor="middle">3</text>
    </g>
    <text class="website" x="383" y="288" text-anchor="middle">www.fuelo-example.us</text>
    <text class="wordmark" x="512" y="256">Fuelo</text>
    <text class="slogan" x="518" y="284">GAS...DELIVERED</text>
    <text class="tagline" x="914" y="176" text-anchor="middle">Say Goodbye to</text>
    <text class="tagline" x="914" y="198" text-anchor="middle">the Gas Station</text>
    <text class="app-note" x="1056" y="175" text-anchor="middle">App download</text>
    <text class="app-note" x="1056" y="187" text-anchor="middle">available on</text>
    <rect class="store-badge" x="1019" y="194" width="76" height="22" rx="3"/>
    <text class="store-name" x="1057" y="209" text-anchor="middle">Storeva</text>
    <rect class="store-badge" x="1019" y="222" width="76" height="22" rx="3"/>
    <text class="store-name" x="1057" y="237" text-anchor="middle">Appnest</text>
  </g>

  <!-- Passenger side layout -->
  <g class="layout-passenger-side">
    <g clip-path="url(#clip-passenger-side)">
      <use href="#truck-side" class="body-panel" transform="translate(1204 428) scale(-1 1)"/>
      <rect class="brand-band" x="719" y="468" width="250" height="270"/>
      <polygon class="tagline-panel" points="226,574 362,572 356,676 216,678"/>
      <polygon class="accent-stripe" points="367,572 372,572 366,676 361,676"/>
      <polygon class="accent-stripe" points="214,574 220,574 210,700 204,700"/>
      <use href="#truck-glass" class="window-area" transform="translate(1204 428) scale(-1 1)"/>
    </g>
    <g class="hazmat-placard" transform="translate(1026 620)">
      <rect class="placard-diamond" x="-19" y="-19" width="38" height="38" transform="rotate(45)"/>
      <rect class="placard-number-box" x="-17" y="-10" width="34" height="17"/>
      <text class="placard-number" x="0" y="4" text-anchor="middle">1203</text>
      <text class="placard-class" x="0" y="20" text-anchor="middle">3</text>
    </g>
    <text class="website" x="820" y="716" text-anchor="middle">www.fuelo-example.us</text>
    <text class="wordmark" x="376" y="684">Fuelo</text>
    <text class="slogan" x="378" y="712">GAS...DELIVERED</text>
    <text class="tagline" x="290" y="604" text-anchor="middle">Say Goodbye to</text>
    <text class="tagline" x="290" y="626" text-anchor="middle">the Gas Station</text>
    <text class="app-note" x="143" y="603" text-anchor="middle">App download</text>
    <text class="app-note" x="143" y="615" text-anchor="middle">available on</text>
    <rect class="store-badge" x="105" y="622" width="76" height="22" rx="3"/>
    <text class="store-name" x="143" y="637" text-anchor="middle">Storeva</text>
    <rect class="store-badge" x="105" y="650" width="76" height="22" rx="3"/>
    <text class="store-name" x="143" y="665" text-anchor="middle">Appnest</text>
  </g>
</svg>
</body>
</html>
```